Want a package created for a new protein bar

We would like a new package created for a new protein bar project The name of the bar will be VORNBar a real food protein bar, we would like a ‘window’ on the package of bar like Brisk Mell bar below in images.

VORNBar
‘Super Food Bar’
14g of Whey Protein
The package film size is the following 12cm width x 15cm Length,
Flavor Peanut Chocolate Chip, additional information will be attached shortly like nutrition facts,

Target Market(s)

fitness market, bodybuilders, athletes, everyday people

Industry/Entity Type

Health Product

Logo Text

VORNBar

Font styles to use
Serif
Sans Serif
Decorative

Requirements
Must have
• Package window

```html
<!DOCTYPE html>
<html lang="en">
<head>
<meta charset="UTF-8">
<title>VORNBar Package Front</title>
<link rel="stylesheet" href="https://fonts.googleapis.com/css2?family=Montserrat:wght@700;800;900&display=swap">
<style>
  :root {
    --orange-deep: #ff7a00;
    --orange-mid: #ff9a0a;
    --orange-gold: #ffc814;
    --red-top: #f01820;
    --red-bottom: #a80808;
    --brown-dark: #3a1c0c;
    --white: #ffffff;
    --window: #000000;
    --milk: #f4f6f6;
    --cookie: #d48a3c;
  }
  * { margin: 0; padding: 0; box-sizing: border-box; }
  html, body { width: 1200px; height: 960px; overflow: hidden; }
  body { font-family: "Montserrat", sans-serif; }
  .package {
    position: relative;
    width: 1200px;
    height: 960px;
    overflow: hidden;
    background:
      radial-gradient(circle at 20% 40%, rgba(255,210,60,.35) 0 90px, transparent 92px),
      radial-gradient(circle at 45% 8%, rgba(255,220,80,.4) 0 70px, transparent 72px),
      radial-gradient(circle at 95% 30%, rgba(255,225,90,.45) 0 80px, transparent 82px),
      radial-gradient(ellipse at 100% 100%, #3a1a08 0, rgba(60,25,5,0) 22%),
      linear-gradient(110deg, var(--orange-deep) 0%, var(--orange-mid) 40%, var(--orange-gold) 70%, #f2a81a 100%);
  }
  .brand-pill {
    position: absolute;
    left: 141px; top: 66px;
    width: 311px; height: 98px;
    border-radius: 49px;
    border: 2px solid var(--white);
    background: linear-gradient(180deg, var(--red-top) 0%, #e8404a 48%, #cc1010 52%, var(--red-bottom) 100%);
    display: flex; align-items: center; justify-content: center;
    color: var(--white);
    font-weight: 900;
    font-size: 48px;
    letter-spacing: 1px;
    text-shadow: 2px 3px 0 #6a0000;
  }
  .product-name {
    position: absolute;
    left: 0; width: 592px; top: 200px;
    text-align: center;
    font-weight: 900;
    font-size: 78px;
    color: var(--brown-dark);
  }
  .tagline {
    position: absolute;
    left: 0; width: 592px; top: 330px;
    text-align: center;
    font-weight: 800;
    font-size: 31px;
    color: var(--white);
    text-shadow: 2px 2px 0 var(--brown-dark);
  }
  .hero-art {
    position: absolute;
    left: 0; top: 372px;
    width: 590px; height: 522px;
  }
  .bar-window {
    position: absolute;
    left: 590px; top: 66px;
    width: 539px; height: 826px;
    border-radius: 34px;
    background: var(--window);
  }
  .protein-claim {
    position: absolute;
    left: 0; width: 580px; top: 900px;
    text-align: center;
    font-weight: 800;
    font-size: 24px;
    color: var(--white);
  }
</style>
</head>
<body>
  <main class="package">
    <div class="brand-pill">BRAND</div>
    <h1 class="product-name">VORNBar</h1>
    <p class="tagline">Super Food Bar</p>
    <svg class="hero-art" viewBox="0 0 590 522" role="img" aria-label="Illustration of peanut chocolate chip cookies and peanuts splashing into milk">
      <defs>
        <radialGradient id="cookieGlow" cx="50%" cy="45%" r="55%">
          <stop offset="0" stop-color="var(--cookie)" stop-opacity=".8"/>
          <stop offset="1" stop-color="var(--cookie)" stop-opacity="0"/>
        </radialGradient>
        <linearGradient id="milkFlow" x1="0" y1="0" x2="0" y2="1">
          <stop offset="0" stop-color="var(--milk)" stop-opacity=".6"/>
          <stop offset="1" stop-color="var(--milk)"/>
        </linearGradient>
      </defs>
      <ellipse cx="300" cy="210" rx="280" ry="200" fill="url(#cookieGlow)"/>
      <path d="M0 265 C90 280 180 360 320 350 C420 340 520 260 590 180 L590 300 C500 380 420 430 300 445 C200 460 80 500 0 522 Z" fill="url(#milkFlow)"/>
    </svg>
    <div class="bar-window"></div>
    <p class="protein-claim">14g of Whey Protein</p>
  </main>
</body>
</html>
```